Business Card

Company: Pine Hollow Nursery.

Use uploaded logo or design one just like it. This is a tree growing operation and really like earth tone colors.

Target Market(s)

Landscaping company's, retail nurseries, and landscape arc.

Industry/Entity Type

Business

Font styles to use
Serif

Requirements
Must have
• Name: Dale Wexford
Title: Owner
Address: 48217 W. 115 Road, Fernbrook, AR 72961
Office: 918-555-3172
Cell: 918-555-6093
Fax: 918-555-4418
email: dalepn@corvalink.net
Pine Hollow Nursery

```html
<!DOCTYPE html>
<html lang="en">
<head>
<meta charset="UTF-8">
<title>Pine Hollow Nursery – Business Card</title>
<link rel="stylesheet" href="https://fonts.googleapis.com/css2?family=Alegreya:wght@400;700;800&display=swap">
<style>
  :root {
    --backdrop: #ebebeb;
    --card-white: #ffffff;
    --leaf-green: #5a7a34;
    --label-green: #74a03f;
    --ink: #1e1e1e;
    --paper-shadow: rgba(0, 0, 0, 0.22);
  }
  html, body {
    margin: 0;
    padding: 0;
    width: 1200px;
    height: 761px;
    overflow: hidden;
    background: var(--backdrop);
    font-family: "Alegreya", Georgia, serif;
  }
  .business-card {
    position: absolute;
    left: 100px;
    top: 95px;
    width: 1000px;
    height: 571px;
    background: var(--card-white);
    box-shadow: 0 6px 18px var(--paper-shadow);
    overflow: hidden;
  }
  .card-art {
    position: absolute;
    inset: 0;
  }
  .brand-mark {
    position: absolute;
    left: 40px;
    top: 175px;
    display: flex;
    align-items: center;
    gap: 12px;
    color: var(--card-white);
    font-size: 22px;
    font-weight: 700;
  }
  .brand-mark .mark-dot {
    width: 18px;
    height: 18px;
    border-radius: 50%;
    background: var(--card-white);
  }
  .contact-block {
    position: absolute;
    left: 430px;
    top: 150px;
    width: 540px;
    text-align: center;
    color: var(--ink);
  }
  .owner-line {
    font-size: 24px;
    margin: 0;
  }
  .owner-name { font-weight: 800; }
  .company-name {
    margin: 4px 0 8px;
    font-size: 42px;
    font-weight: 800;
    letter-spacing: 1px;
    text-transform: uppercase;
    color: var(--leaf-green);
  }
  .contact-line {
    margin: 0 0 4px;
    font-size: 17px;
  }
  .contact-label { color: var(--label-green); }
  .address-line {
    position: absolute;
    left: 40px;
    top: 448px;
    margin: 0;
    color: var(--card-white);
    font-size: 28px;
  }
</style>
</head>
<body>
  <div class="business-card">
    <svg class="card-art" width="1000" height="571" viewBox="0 0 1000 571" aria-hidden="true">
      <path fill="var(--leaf-green)" d="M0 0 H410 C345 60 385 145 320 225 C265 295 200 340 195 430 H0 Z"/>
      <rect fill="var(--leaf-green)" x="0" y="430" width="1000" height="92"/>
    </svg>

    <div class="brand-mark">
      <span class="mark-dot"></span>
      <span>Pine Hollow Nursery</span>
    </div>

    <div class="contact-block">
      <p class="owner-line"><span class="owner-name">Dale Wexford</span> (Owner)</p>
      <h1 class="company-name">Pine Hollow Nursery</h1>
      <p class="contact-line">
        <span class="contact-label">Office:</span> 918-555-3172,
        <span class="contact-label">Cell:</span> 918-555-6093,
        <span class="contact-label">Fax:</span> 918-555-4418
      </p>
      <p class="contact-line">
        <span class="contact-label">Email:</span> dalepn@corvalink.net
      </p>
    </div>

    <p class="address-line">Address : 48217 W. 115 Road, Fernbrook, AR 72961</p>
  </div>
</body>
</html>
```